Fresh easy to read restaurant menu

Burger Restaurant menu based on an island in Thailand. Light colours because we have dimmed lights and it needs to be easy to read. Need to fit on A3 size paper/ 2 sides. COULD BE LANDSCAPE POSITION TOO.
Colour choices around existing logo. Vintage fun look if possible. Owner needs to be able to change text when menu needs to change.
Have different major sections (Starters - Juicy burgers and sandwiches - Crunchy salads - Tasty meals - Sweet bites & desserts) smaller sections (Extras - Dips, mayos and more - Zindle's special thirst quenchers)
I uploaded my last menu design. I need a fresh look as we have used this last one for the past 4 years.
Please make sure it's not too dark and easy to read. LANDSCAPE is better. The menu items needs to the editable because we are located on a thai island and products are not always available. Prices needs constant changes too as we have low and high seasons.
Thanks for your time and effort.
Reason: Still looking for the right design. Some designers have committed but not enough time to submit designs.
Restaurant

```html
<!DOCTYPE html>
<html lang="en">
<head>
<meta charset="utf-8">
<title>Zindle's Menu</title>
<link rel="stylesheet" href="https://fonts.googleapis.com/css2?family=Lobster&family=Roboto+Condensed:wght@400;700&display=swap">
<style>
:root{
  --wood-light:#f1e2c9;
  --wood-mid:#e6d1b0;
  --ink:#3b2c20;
  --ink-soft:#4d3e32;
  --teal:#82d0c8;
  --teal-dark:#5fb3aa;
  --orange:#f2955a;
  --orange-line:#e2763a;
  --orange-title:#b7452a;
  --sky:#8fcdea;
  --sky-line:#e9f6fb;
  --brand:#c4622b;
  --badge:#c8bfb4;
  --white:#ffffff;
}
*{margin:0;padding:0;box-sizing:border-box}
html,body{width:1200px;height:848px;overflow:hidden}
body{font-family:"Roboto Condensed",Arial,sans-serif;color:var(--ink)}
.menu{position:relative;width:1200px;height:848px;
  background:linear-gradient(90deg,var(--wood-light),var(--wood-mid) 30%,var(--wood-light) 55%,var(--wood-mid) 80%,var(--wood-light));}
.column{position:absolute;top:0;height:848px}
.col-starters{left:26px;width:310px}
.col-burgers{left:420px;width:330px}
.col-toasted{left:818px;width:352px}

.ribbon{position:absolute;height:70px}
.ribbon svg{position:absolute;inset:0;width:100%;height:100%}
.ribbon-title{position:absolute;left:0;right:0;top:14px;text-align:center;
  font-family:"Lobster",cursive;color:var(--white);font-size:19px}

.thb{position:absolute;width:24px;height:24px;border-radius:50%;background:var(--badge);
  color:var(--white);font-size:9px;font-weight:700;line-height:24px;text-align:center}

.item{position:absolute;left:0;right:0;top:var(--y)}
.item-row{display:flex;justify-content:space-between;font-weight:700;font-size:15.5px;line-height:18px}
.item-desc{font-size:12px;line-height:15.5px;color:var(--ink-soft);margin-top:3px;padding-right:20px}
.extra-price{font-weight:700;margin-left:12px}

.brand{position:absolute;left:0;right:0;top:52px;text-align:center;
  font-weight:700;font-size:86px;line-height:90px;color:var(--brand);letter-spacing:1px}
.menu-badge{position:absolute;left:114px;top:195px;width:114px;height:52px}
.menu-badge svg{position:absolute;inset:0}
.menu-badge span{position:absolute;left:0;right:0;top:6px;text-align:center;color:var(--white);
  font-weight:700;font-size:19px}
.burger-intro{position:absolute;left:40px;right:30px;top:302px;text-align:center;
  font-weight:700;font-size:11.5px;line-height:15px}

.box{position:absolute;left:0;width:352px}
.box-title{position:absolute;left:10px;top:-12px;padding:0 6px;font-family:"Lobster",cursive;font-size:18px}
.box-extras{top:340px;height:156px;background:var(--orange);border:2px solid var(--orange-line)}
.box-extras .box-title{color:var(--orange-title);background:var(--wood-light);left:6px}
.extras-list{position:absolute;left:14px;right:36px;top:20px;list-style:none;color:var(--white);font-weight:700;font-size:15px;line-height:18.5px}
.extras-list li{display:flex;justify-content:space-between;flex-wrap:wrap}
.extras-list small{width:100%;font-weight:400;font-size:11.5px;line-height:13px}

.box-sauces{top:536px;height:272px;background:var(--sky);border:2px solid var(--sky-line)}
.box-sauces .box-title{left:72px;top:-14px;color:var(--white);background:var(--sky)}
.sauces-lead{position:absolute;left:0;right:0;top:20px;text-align:center;color:var(--white);font-weight:700;font-size:11.5px}
.sauce-list{position:absolute;left:20px;top:44px;list-style:none;color:var(--white);font-weight:700;font-size:15.5px;line-height:21.5px}
.sauce-brace{position:absolute;left:194px;top:46px;width:20px;height:230px}
.sauce-prices{position:absolute;left:228px;top:110px;width:100px;list-style:none;color:var(--white);font-weight:700;font-size:15.5px;line-height:27px}
.sauce-prices li{display:flex;justify-content:space-between}
</style>
</head>
<body>
<main class="menu">

  <section class="column col-starters">
    <div class="ribbon" style="left:10px;top:26px;width:318px">
      <svg viewBox="0 0 318 70" preserveAspectRatio="none" aria-hidden="true">
        <path d="M0 30 L40 30 L40 72 L0 72 L14 51 Z" fill="var(--teal-dark)"/>
        <path d="M318 30 L278 30 L278 72 L318 72 L304 51 Z" fill="var(--teal-dark)"/>
        <path d="M26 14 Q159 2 292 14 L292 56 Q159 44 26 56 Z" fill="var(--teal)"/>
      </svg>
      <div class="ribbon-title">Starters</div>
    </div>
    <div class="thb" style="left:280px;top:102px">THB</div>

    <div class="item" style="--y:129px"><div class="item-row"><span>Homemade Fries</span><span>70</span></div></div>
    <div class="item" style="--y:164px"><div class="item-row"><span>Battered Onion bunch with dip</span><span>100</span></div></div>
    <div class="item" style="--y:204px"><div class="item-row"><span>Indian Roasted Chickpeas</span><span>60</span></div>
      <p class="item-desc">A low fat and nutritious beer snack!</p></div>
    <div class="item" style="--y:261px"><div class="item-row"><span>Crispy Raviolis</span><span>90</span></div>
      <p class="item-desc">Served with marinara sauce</p></div>
    <div class="item" style="--y:311px"><div class="item-row"><span>Yummy Hummus</span><span>120</span></div>
      <p class="item-desc">Served with crackers &amp; veggies</p></div>
    <div class="item" style="--y:367px"><div class="item-row"><span>Hummus Plate</span><span>180</span></div>
      <p class="item-desc">Meal size portion with a choice of one topping: Feta, chicken, bacon, olives, jalapenos, mushrooms, fried onions or roasted chickpeas<br>Served with crackers &amp; veggies</p></div>
    <div class="item" style="--y:474px"><div class="item-row"><span>Smoked&nbsp; Salmon Starter</span><span>140</span></div>
      <p class="item-desc">Served on cucumber slices with dill cream cheese</p></div>
    <div class="item" style="--y:523px"><div class="item-row"><span>Chicken Wings</span><span>130</span></div>
      <p class="item-desc" style="margin-top:6px">Regular or Super spicy<br>Extra blue cheese dip <span class="extra-price" style="margin-left:2px">30</span></p></div>
    <div class="item" style="--y:589px"><div class="item-row"><span>Garlic Bread</span><span>80</span></div>
      <p class="item-desc">Extra cheese <span class="extra-price">40</span></p></div>
    <div class="item" style="--y:637px"><div class="item-row"><span>Warm Cheese Dip</span><span>150</span></div>
      <p class="item-desc">Served with baked tortilla chips</p></div>
    <div class="item" style="--y:685px"><div class="item-row"><span>Poutine</span><span>130</span></div>
      <p class="item-desc" style="line-height:18px">French fries, gravy &amp; cheese... The most popular munchies from Québec, Canada!<br>
      Extra minced beef <span class="extra-price" style="margin-left:28px">60</span><br>
      Extra pulled pork, chicken or bacon <span class="extra-price" style="margin-left:44px">50</span><br>
      Mexican Style <span class="extra-price" style="margin-left:28px">50</span><br>
      (jalapenos, onions, tomatoes and sour cream)</p></div>
  </section>

  <section class="column col-burgers">
    <h1 class="brand">Zindle</h1>
    <div class="menu-badge">
      <svg viewBox="0 0 114 52" aria-hidden="true">
        <path d="M0 0 L114 0 L114 30 L57 52 L0 30 Z" fill="var(--brand)"/>
        <path d="M5 4 L109 4 L109 27 L57 46 L5 27 Z" fill="var(--orange)"/>
      </svg>
      <span>MENU</span>
    </div>

    <div class="ribbon" style="left:10px;top:250px;width:310px;transform:rotate(-3deg)">
      <svg viewBox="0 0 310 70" preserveAspectRatio="none" aria-hidden="true">
        <path d="M0 30 L38 30 L38 72 L0 72 L14 51 Z" fill="var(--teal-dark)"/>
        <path d="M310 30 L272 30 L272 72 L310 72 L296 51 Z" fill="var(--teal-dark)"/>
        <path d="M24 16 Q155 2 286 16 L286 56 Q155 42 24 56 Z" fill="var(--teal)"/>
      </svg>
      <div class="ribbon-title">Juicy burgers and sandwiches</div>
    </div>
    <p class="burger-intro">Available with first quality BEEF,<br>grilled CHICKEN breast or<br>homemade VEGGIE patty.<br>Served with fries and coleslaw.<br>Get a POUTINE side instead for an extra 50b.</p>
    <div class="thb" style="left:302px;top:368px">THB</div>

    <div class="item" style="--y:400px"><div class="item-row"><span>The Classic</span><span>170</span></div></div>
    <div class="item" style="--y:428px"><div class="item-row"><span>The Cheesy Cheddar</span><span>190</span></div></div>
    <div class="item" style="--y:453px"><div class="item-row"><span>The Hotty</span><span>190</span></div>
      <p class="item-desc">With chili mayo &amp; jalapenos... Hot!</p></div>
    <div class="item" style="--y:493px"><div class="item-row"><span>The Vic's</span><span>200</span></div>
      <p class="item-desc">With blue cheese, fried onions &amp; mushrooms</p></div>
    <div class="item" style="--y:533px"><div class="item-row"><span>The Med</span><span>200</span></div>
      <p class="item-desc">With feta, slow-roasted tomatoes, olive tapenade &amp; hummus</p></div>
    <div class="item" style="--y:577px"><div class="item-row"><span>The Deluxe</span><span>210</span></div>
      <p class="item-desc" style="margin-top:6px">With bacon, homemade mayonnaise &amp; brie cheese</p></div>
    <div class="item" style="--y:620px"><div class="item-row"><span>The&nbsp; ZINDLE</span><span>220</span></div>
      <p class="item-desc" style="padding-right:50px">With onion rings, bacon, sweet BBQ sauce &amp; thousand island dressing</p></div>
    <div class="item" style="--y:679px"><div class="item-row"><span>The Pizza</span><span>220</span></div>
      <p class="item-desc">Pepperoni, mozzarella, pizza sauce &amp; mushrooms</p></div>
    <div class="item" style="--y:722px"><div class="item-row"><span>The&nbsp; Animal</span><span>250</span></div>
      <p class="item-desc" style="padding-right:50px">Two beef patties, BBQ sauce, pickles, coleslaw, egg &amp; crispy onions</p></div>
    <div class="item" style="--y:780px"><div class="item-row"><span>The Fat Betty</span><span>250</span></div>
      <p class="item-desc">Double beef patty with melting cheese middle.</p></div>
  </section>

  <section class="column col-toasted">
    <div class="ribbon" style="left:10px;top:26px;width:330px">
      <svg viewBox="0 0 330 70" preserveAspectRatio="none" aria-hidden="true">
        <path d="M0 30 L40 30 L40 72 L0 72 L14 51 Z" fill="var(--teal-dark)"/>
        <path d="M330 30 L290 30 L290 72 L330 72 L316 51 Z" fill="var(--teal-dark)"/>
        <path d="M26 14 Q165 2 304 14 L304 56 Q165 44 26 56 Z" fill="var(--teal)"/>
      </svg>
      <div class="ribbon-title">ToastedSandwiches</div>
    </div>
    <div class="thb" style="left:294px;top:108px">THB</div>

    <div class="item" style="--y:139px;right:30px"><div class="item-row"><span>Jalapeno Grilled Cheese</span><span>160</span></div>
      <p class="item-desc">Cream cheese, cheddar, marinara sauce &amp; green onion<br>Extra bacon <span class="extra-price" style="margin-left:4px">40</span></p></div>
    <div class="item" style="--y:207px;right:30px"><div class="item-row"><span>Pulled Pork Sandwich</span><span>190</span></div>
      <p class="item-desc" style="padding-right:0">Slow-roasted pork &amp; mozzarella sandwich toasted on the grill</p></div>
    <div class="item" style="--y:252px;right:30px"><div class="item-row"><span>Patty Melt</span><span>190</span></div>
      <p class="item-desc" style="padding-right:0;white-space:nowrap;margin-top:6px">With thin beef patty, fried onions, cheddar &amp; thousandisland dressing</p></div>

    <div class="box box-extras">
      <h2 class="box-title">Make your BURGER Extra Special with...</h2>
      <ul class="extras-list">
        <li><span>Fried Onions or Mushrooms</span><span>30</span></li>
        <li><span>Cheese</span><span>40</span><small>(Cheddar, Feta, Brie, Blue,Mozz or Cream Cheese)</small></li>
        <li style="margin-top:4px"><span>Bacon or Pepperoni</span><span>40</span></li>
        <li><span>Pickles or Jalapenos</span><span>20</span></li>
        <li><span>Fried Egg</span><span>20</span></li>
        <li><span>Smoked Salmon</span><span>60</span></li>
      </ul>
    </div>

    <div class="box box-sauces">
      <h2 class="box-title">Mayo, Dips &amp; More.....</h2>
      <p class="sauces-lead">Pimp up your fries and burgers with our tasty homemade sauces</p>
      <ul class="sauce-list">
        <li>Chili Mayo</li><li>Garlic Mayo</li><li>Ranch Mayo</li><li>Honey Mustard Mayo</li>
        <li>Sweet BBQ Sauce</li><li>Blue Cheese Dip</li><li>Thousand Island Dressing</li>
        <li style="line-height:19px">Hummus</li><li style="line-height:19px">Gravy</li><li>Marinara Sauce</li>
      </ul>
      <svg class="sauce-brace" viewBox="0 0 20 230" aria-hidden="true">
        <path d="M4 2 Q14 4 12 20 L10 96 Q10 112 18 115 Q10 118 10 134 L12 210 Q14 226 4 228" fill="none" stroke="var(--white)" stroke-width="1.5"/>
      </svg>
      <ul class="sauce-prices">
        <li><span>Single</span><span>30</span></li>
        <li><span style="padding-left:14px">Duo</span><span>50</span></li>
        <li><span style="padding-left:16px">Trio</span><span>70</span></li>
      </ul>
    </div>
  </section>

</main>
</body>
</html>
```